Create a pitch deck for a specialist physical product development search firm

Please review the attached project brief and the following instructions.
I need a designer to create a 10-slide pitch deck for Vemra, a specialist recruitment partner for physical product design & development companies. The deck will be used to pitch our retained/exclusive recruitment service to potential clients.
The design should:
Follow our bold, clean brand guidelines (provided)
Feel premium, minimalist, and professional
The deck includes:
Problem statement
Our story & differentiators
Process overview
2 client case studies
Social proof/testimonials
Clear call-to-action
Deliverables:
Editable Canva file (preferred) or PowerPoint
Exported PDF
Optional: LinkedIn carousel adaptation
Look and feel
Each slider illustrates characteristics of the customer's brand and the style your logo design should communicate.

```html
<!DOCTYPE html>
<html lang="en">
<head>
<meta charset="utf-8">
<title>Vemra Pitch Deck</title>
<link href="https://fonts.googleapis.com/css2?family=Poppins:wght@300;400;500;600;700&display=swap" rel="stylesheet">
<style>
:root{
  --bg:#575757;
  --white:#ffffff;
  --ink:#1d1d1f;
  --text:#2b2b2b;
  --muted:#555555;
  --amber:#F0AC33;
  --orange:#D87B0A;
  --dark:#2B2E31;
  --line:#dddddd;
  --soft:#F8E8CB;
  --faint:#f4f1ec;
}
*{margin:0;padding:0;box-sizing:border-box}
html,body{width:994px;height:1200px;overflow:hidden}
body{background:var(--bg);font-family:"Poppins",sans-serif;color:var(--text);position:relative}
.slide{position:absolute;width:435px;height:244px;background:var(--white);overflow:hidden}
.slide > *{position:absolute}
.col-l{left:43px}.col-r{left:516px}
.row-1{top:38px}.row-2{top:325px}.row-3{top:612px}.row-4{top:899px}
.pattern-band{left:0;right:0;bottom:0;height:34px;background:linear-gradient(to bottom,rgba(244,241,236,0),var(--faint))}
.bars{left:22px;top:6px;width:36px;height:2px}
.bars::before,.bars::after{content:"";position:absolute;top:0;height:2px}
.bars::before{left:0;width:20px;background:var(--amber)}
.bars::after{left:23px;width:13px;background:var(--orange)}
.title{left:22px;top:9px;font-size:14.5px;font-weight:600;color:var(--ink);white-space:nowrap;letter-spacing:.1px}
.subtitle{left:22px;font-size:8.6px;font-weight:400;color:var(--ink);white-space:nowrap}
.brand{right:22px;top:4px;display:flex;align-items:center;gap:4px}
.brand .mark{width:12px;height:12px;background:var(--orange)}
.brand .name{font-size:13px;font-weight:600;color:var(--ink);line-height:1}
.icon{border-radius:50%;display:flex;align-items:center;justify-content:center}
.icon.amber{background:var(--amber)}.icon.orange{background:var(--orange)}.icon.dark{background:var(--dark)}
/* welcome */
.hero-brand{left:22px;top:50px;display:flex;align-items:center;gap:14px}
.hero-brand .mark{width:38px;height:38px;background:var(--orange)}
.hero-brand .name{font-size:36px;font-weight:500;color:var(--ink);line-height:1}
.hero-title{left:21px;top:108px;font-size:19px;font-weight:700;color:var(--ink);white-space:nowrap}
.hero-sub{left:21px;top:137px;font-size:10px;line-height:18px;color:var(--ink)}
.social{top:179px;width:18px;height:18px;border:1.2px solid var(--amber);border-radius:50%}
.hero-visual{left:230px;top:31px;width:184px;height:184px;background:linear-gradient(135deg,#9a9a9a 0%,#cfcfcf 45%,var(--orange) 46%,var(--orange) 100%)}
/* problem */
.problem-card{width:93px;height:66px;border:1px solid var(--amber);border-radius:0 0 18px 0;text-align:center;padding:26px 4px 0;font-size:5.6px;line-height:1.85;color:var(--ink)}
.problem-card .icon{position:absolute;width:34px;height:34px;left:29px;top:-15px}
/* story */
.story-lead{left:21px;top:36px;font-size:8.6px;font-weight:500;color:var(--ink);white-space:nowrap}
.story-body{left:22px;top:54px;width:192px;font-size:6.2px;line-height:11px;color:var(--text)}
.story-body p{margin-bottom:11px}
.story-body b{font-weight:600;color:var(--ink)}
.about-head{left:234px;top:36px;font-size:8.6px;font-weight:500;color:var(--ink)}
.about-item{left:235px;width:160px;display:flex;align-items:center;gap:4px;font-size:6.8px;line-height:10.5px;color:var(--ink)}
.about-item .icon{width:24px;height:24px;flex:none}
.divider{height:1px;background:var(--line)}
/* who we help */
.help-card{top:64px;width:117px;height:124px;color:var(--white);padding:45px 12px 0 14px}
.help-card .icon{position:absolute;left:14px;top:10px;width:27px;height:27px;background:var(--white)}
.help-card h3{font-size:7px;font-weight:600;margin-bottom:3px}
.help-card ul{list-style:none}
.help-card li{position:relative;font-size:5.3px;line-height:11px;padding-left:6px}
.help-card li::before{content:"";position:absolute;left:0;top:4px;width:3px;height:3px;border-radius:50%;background:var(--white)}
.card-amber{left:22px;background:var(--amber);border-radius:0 24px 24px 0}
.card-dark{left:159px;background:var(--dark);border-radius:24px 24px 0 0}
.card-orange{left:295px;background:var(--orange);border-radius:24px 0 24px 24px}
/* deliver */
.step{left:25px;display:flex;align-items:flex-start;gap:7px;width:175px}
.step .icon{width:24px;height:24px;flex:none}
.step p{font-size:5.8px;line-height:10.5px;color:var(--ink)}
.step b{font-size:8.4px;font-weight:500}
.stat{font-size:6.6px;font-weight:500;color:var(--ink);display:flex;align-items:center;gap:4px;white-space:nowrap}
.stat i{width:6px;height:6px;border-radius:50%;background:var(--amber);display:inline-block}
.quote-box{left:230px;width:172px;height:66px;border:1px solid var(--amber);padding:18px 10px 0}
.quote-box .icon{position:absolute;left:14px;top:-9px;width:17px;height:17px;color:var(--white);font-size:10px;font-weight:700;line-height:1}
.quote-box q{display:block;font-size:5.4px;font-weight:600;line-height:11px;color:var(--ink);quotes:"\201C" "\201D"}
.quote-box cite{display:block;font-style:normal;font-size:4.2px;margin-top:6px;color:var(--muted)}
/* partnership timeline */
.tl-label{width:110px;margin-left:-55px;text-align:center;font-size:6.8px;line-height:12.5px;color:var(--ink)}
.tl-line{left:18px;top:115px;width:395px;height:1px;background:#888}
.tl-node{width:32px;height:32px;margin:-16px 0 0 -16px;top:115px}
.tl-node.light{background:var(--amber)}
.tl-bottom-band{left:0;right:0;bottom:0;height:29px;background:var(--soft)}
/* partnership clients */
.group-head{font-size:7.4px;font-weight:600;color:var(--ink)}
.group-list{font-size:5.3px;line-height:12.5px;color:var(--ink);white-space:nowrap}
.photo-area{left:271px;top:122px;width:95px;height:95px;background:linear-gradient(135deg,#bdbdbd,#6e6e6e)}
/* call to action */
.cta-head{left:21px;top:37px;font-size:9.8px;font-weight:600;color:var(--ink)}
.cta-sub{left:21px;top:53px;font-size:6.6px;color:var(--muted)}
.cta-quote{left:22px;top:83px;width:175px;font-size:6.4px;line-height:11px;color:var(--ink)}
.cta-cite{left:22px;top:120px;font-size:5px;color:var(--muted)}
.cta-btn{left:21px;top:139px;width:61px;height:16px;background:var(--orange);border-radius:0 6px 0 0;color:var(--white);font-size:6.8px;font-weight:500;display:flex;align-items:center;justify-content:center}
.cta-visual{left:234px;top:44px;width:157px;height:157px;background:linear-gradient(160deg,var(--amber),var(--orange))}
.qmark{font-size:16px;font-weight:700;color:var(--amber);line-height:1}
</style>
</head>
<body>

<section class="slide col-l row-1">
  <div class="pattern-band"></div>
  <div class="hero-brand"><span class="mark"></span><span class="name">vemra</span></div>
  <h1 class="hero-title">Welcome to Vemra</h1>
  <p class="hero-sub">Specialist Search for Physical Product<br>Design &amp; Development</p>
  <span class="social" style="left:22px"></span>
  <span class="social" style="left:45px"></span>
  <span class="social" style="left:67px"></span>
  <div class="hero-visual" role="img" aria-label="Black and white photographs of engineers at work, set in an orange geometric frame"></div>
</section>

<section class="slide col-r row-1">
  <div class="pattern-band"></div>
  <span class="bars"></span>
  <h2 class="title">The Problem</h2>
  <p class="subtitle" style="top:30px">Why recruitment feels broken</p>
  <div class="brand"><span class="mark"></span><span class="name">vemra</span></div>

  <div class="problem-card" style="left:52px;top:62px"><span class="icon orange"><svg width="14" height="14" viewBox="0 0 14 14"><rect x="3" y="2" width="8" height="10" fill="none" stroke="#fff" stroke-width="1.3"/><path d="M5 5h4M5 7.5h4M5 10h2" stroke="#fff" stroke-width="1.1"/></svg></span>High-volume,<br>transactional models lead<br>to disengagement</div>
  <div class="problem-card" style="left:173px;top:62px"><span class="icon orange"><svg width="14" height="14" viewBox="0 0 14 14"><circle cx="7" cy="4.5" r="2.2" fill="#fff"/><path d="M2.5 12c0-3 2-4.5 4.5-4.5s4.5 1.5 4.5 4.5z" fill="#fff"/></svg></span>Lack of true partnership<br>between clients &amp;<br>recruiters</div>
  <div class="problem-card" style="left:294px;top:62px"><span class="icon amber"><svg width="14" height="14" viewBox="0 0 14 14"><rect x="2.5" y="2" width="9" height="10" rx="1" fill="#fff"/></svg></span>Time wasted screening<br>irrelevant CVs</div>
  <div class="problem-card" style="left:107px;top:138px"><span class="icon orange"><svg width="14" height="14" viewBox="0 0 14 14"><circle cx="4" cy="5" r="1.7" fill="#fff"/><circle cx="10" cy="5" r="1.7" fill="#fff"/><path d="M1.5 11c0-2 1.2-3 2.5-3s2.5 1 2.5 3zM7.5 11c0-2 1.2-3 2.5-3s2.5 1 2.5 3z" fill="#fff"/></svg></span>Poor candidate journeys =<br>poor hiring outcomes</div>
  <div class="problem-card" style="left:228px;top:138px"><span class="icon amber"><svg width="14" height="14" viewBox="0 0 14 14"><circle cx="6" cy="6" r="3.3" fill="none" stroke="#fff" stroke-width="1.4"/><path d="M8.5 8.5l3 3" stroke="#fff" stroke-width="1.5"/></svg></span>Recruiters who don’t “get”<br>the market or what good<br>looks like</div>
</section>

<section class="slide col-l row-2">
  <div class="pattern-band" style="height:70px"></div>
  <span class="bars"></span>
  <h2 class="title">The Vemra Story</h2>
  <div class="brand"><span class="mark"></span><span class="name">vemra</span></div>
  <p class="story-lead">Vemra means chord. It’s about harmony.</p>
  <div class="story-body">
    <p><b>Vemra</b> comes from the old word Vemre, meaning chord—a symbol of harmony where individual notes create something greater.</p>
    <p>I founded Vemra to bring this principle into recruitment. Too often, traditional recruitment feels transactional: <b>high volume, low engagement, and little understanding</b> of what makes a team resonate.At <b>Vemra</b>, we help hardware brands, consultancies, and medtech innovators build teams that thrive.</p>
  </div>
  <p class="about-head">Vemra is about:</p>
  <div class="about-item" style="top:55px"><span class="icon amber"><svg width="12" height="12" viewBox="0 0 12 12"><path d="M2 6l2.5 2.5L10 3" fill="none" stroke="#fff" stroke-width="1.5"/></svg></span><span>Relationships over transactions</span></div>
  <div class="divider" style="left:236px;top:91px;width:158px"></div>
  <div class="about-item" style="top:101px"><span class="icon orange"><svg width="12" height="12" viewBox="0 0 12 12"><path d="M2 3h8M2 6h8M2 9h5" stroke="#fff" stroke-width="1.3"/></svg></span><span>Speaking your language, knowing your market</span></div>
  <div class="divider" style="left:236px;top:137px;width:158px"></div>
  <div class="about-item" style="top:147px"><span class="icon dark"><svg width="12" height="12" viewBox="0 0 12 12"><circle cx="6" cy="6" r="3.8" fill="none" stroke="#fff" stroke-width="1.3"/><path d="M6 4v2.2l1.5 1" stroke="#fff" stroke-width="1.1" fill="none"/></svg></span><span>Creating lasting impact for candidates and clients</span></div>
</section>

<section class="slide col-r row-2">
  <div class="pattern-band" style="height:44px"></div>
  <span class="bars"></span>
  <h2 class="title">Who We Help</h2>
  <p class="subtitle" style="top:35px">Who we help &amp; what success looks like</p>
  <div class="brand"><span class="mark"></span><span class="name">vemra</span></div>

  <div class="help-card card-amber"><span class="icon"><svg width="14" height="14" viewBox="0 0 14 14"><circle cx="7" cy="5" r="2.2" fill="#F0AC33"/><path d="M3 12c0-3 2-4 4-4s4 1 4 4z" fill="#F0AC33"/></svg></span>
    <h3>Typical Clients</h3>
    <ul><li>Hardware start-ups &amp;<br>scale-ups</li><li>Design consultancies</li><li>Medtech &amp; consumer health<br>brands</li></ul></div>
  <div class="help-card card-dark"><span class="icon"><svg width="14" height="14" viewBox="0 0 14 14"><path d="M3 11V7M6 11V5M9 11V8M12 11V3" stroke="#2B2E31" stroke-width="1.6"/></svg></span>
    <h3>Challenges</h3>
    <ul><li>Long hiring cycles</li><li>Low candidate engagement</li><li>Difficulty finding niche talent</li></ul></div>
  <div class="help-card card-orange"><span class="icon"><svg width="14" height="14" viewBox="0 0 14 14"><circle cx="7" cy="7" r="5" fill="#D87B0A"/><path d="M4.5 7l1.8 1.8L9.7 5.4" stroke="#fff" stroke-width="1.3" fill="none"/></svg></span>
    <h3>What success looks like</h3>
    <ul><li>Hiring within 3–6 weeks</li><li>Candidates aligned &amp; excited</li><li>Predictable process &amp; higher<br>retention</li></ul></div>
</section>

<section class="slide col-l row-3">
  <div class="pattern-band"></div>
  <span class="bars"></span>
  <h2 class="title">How We Deliver</h2>
  <p class="subtitle" style="top:33px">A partnership-led process that works</p>
  <div class="brand"><span class="mark"></span><span class="name">vemra</span></div>

  <svg style="left:20px;top:75px" width="20" height="80" viewBox="0 0 20 80"><path d="M12 0C2 12 2 28 12 36M12 46C2 58 2 72 12 80" fill="none" stroke="#888" stroke-width=".6" stroke-dasharray="1.5 1.5"/></svg>
  <div class="step" style="top:51px"><span class="icon amber"><svg width="12" height="12" viewBox="0 0 12 12"><circle cx="6" cy="6" r="3.8" fill="none" stroke="#fff" stroke-width="1.3"/><circle cx="6" cy="6" r="1.3" fill="#fff"/></svg></span><p><b>Define:</b> Understand your business, team<br>culture &amp; goals</p></div>
  <div class="step" style="top:102px"><span class="icon dark"><svg width="12" height="12" viewBox="0 0 12 12"><circle cx="4" cy="4.5" r="1.5" fill="#fff"/><circle cx="8" cy="4.5" r="1.5" fill="#fff"/><path d="M1.5 10c0-2 1-3 2.5-3s2.5 1 2.5 3zM5.5 10c0-2 1-3 2.5-3s2.5 1 2.5 3z" fill="#fff"/></svg></span><p><b>Engage:</b> Exclusive, tailored candidate<br>journeys</p></div>
  <div class="step" style="top:153px"><span class="icon orange"><svg width="12" height="12" viewBox="0 0 12 12"><rect x="1.5" y="3.5" width="6" height="4.5" fill="#fff"/><path d="M7.5 5h2l1.5 1.5V8h-3.5z" fill="#fff"/><circle cx="3.5" cy="9" r="1" fill="#fff"/><circle cx="9" cy="9" r="1" fill="#fff"/></svg></span><p><b>Deliver:</b> Predictable outcomes with high<br>engagement</p></div>

  <p class="stat" style="left:29px;top:192px"><i></i>100% fill rate</p>
  <p class="stat" style="left:91px;top:192px"><i></i>97% retention after 12 months</p>
  <p class="stat" style="left:29px;top:210px"><i></i>+92 NPS (world-class)</p>

  <div class="quote-box" style="top:47px"><span class="icon orange">”</span>
    <q>No agency shenanigans – helped us build a professional hiring experience.</q>
    <cite>— Tom Harlow, Co-Founder, Fieldline Instruments</cite></div>
  <div class="quote-box" style="top:135px"><span class="icon orange">”</span>
    <q>Compared to other recruiters, this was faster, more personalised, and highly organised.</q>
    <cite>— Nina Castell, CEO, Brightwell Health</cite></div>
</section>

<section class="slide col-r row-3">
  <div class="tl-bottom-band" role="img" aria-label="Soft decorative band of pale amber geometric shapes"></div>
  <span class="bars"></span>
  <h2 class="title">How Our Partnership Works</h2>
  <div class="brand"><span class="mark"></span><span class="name">vemra</span></div>

  <p class="tl-label" style="left:62px;top:47px">Exclusive search<br>(no spray &amp; pray)</p>
  <p class="tl-label" style="left:188px;top:47px">Founder-led<br>recruitment process</p>
  <p class="tl-label" style="left:313px;top:47px">Guaranteed project<br>completion</p>
  <svg style="left:57px;top:82px" width="10" height="8" viewBox="0 0 10 8"><path d="M1 1l4 6 4-6" fill="none" stroke="#D87B0A" stroke-width="1.6"/></svg>
  <svg style="left:183px;top:82px" width="10" height="8" viewBox="0 0 10 8"><path d="M1 1l4 6 4-6" fill="none" stroke="#2B2E31" stroke-width="1.6"/></svg>
  <svg style="left:308px;top:82px" width="10" height="8" viewBox="0 0 10 8"><path d="M1 1l4 6 4-6" fill="none" stroke="#D87B0A" stroke-width="1.6"/></svg>

  <div class="tl-line"></div>
  <svg style="left:16px;top:112px" width="6" height="6" viewBox="0 0 6 6"><path d="M0 0l6 3-6 3 2-3z" fill="#222"/></svg>
  <svg style="left:411px;top:112px" width="6" height="6" viewBox="0 0 6 6"><path d="M0 0l6 3-6 3 2-3z" fill="#222"/></svg>

  <span class="icon orange tl-node" style="left:62px"><svg width="16" height="16" viewBox="0 0 16 16"><circle cx="8" cy="8" r="6" fill="none" stroke="#fff" stroke-width="1.3"/><rect x="3" y="6.5" width="10" height="3" fill="#fff"/></svg></span>
  <span class="icon tl-node light" style="left:125px"><svg width="16" height="16" viewBox="0 0 16 16"><rect x="4" y="6" width="8" height="7" fill="#fff"/><path d="M4 6l4-3 4 3" fill="none" stroke="#fff" stroke-width="1.2"/></svg></span>
  <span class="icon dark tl-node" style="left:188px"><svg width="16" height="16" viewBox="0 0 16 16"><circle cx="8" cy="7" r="3.5" fill="none" stroke="#fff" stroke-width="1.3"/><path d="M6.5 7l1 1 2-2" stroke="#fff" stroke-width="1" fill="none"/><path d="M3 13h10" stroke="#fff" stroke-width="1.2"/></svg></span>
  <span class="icon tl-node light" style="left:251px"><svg width="16" height="16" viewBox="0 0 16 16"><circle cx="8" cy="8" r="5.5" fill="none" stroke="#fff" stroke-width="1.3"/><text x="8" y="10.8" font-size="7.5" font-family="Poppins,sans-serif" font-weight="600" fill="#fff" text-anchor="middle">$</text></svg></span>
  <span class="icon orange tl-node" style="left:314px"><svg width="16" height="16" viewBox="0 0 16 16"><rect x="4" y="3" width="8" height="10" fill="none" stroke="#fff" stroke-width="1.2"/><path d="M6 6h4M6 8.5h4M6 11h2" stroke="#fff" stroke-width="1"/></svg></span>
  <span class="icon dark tl-node" style="left:377px"><svg width="16" height="16" viewBox="0 0 16 16"><path d="M8 2l5 2v4c0 3-2.3 5-5 6-2.7-1-5-3-5-6V4z" fill="none" stroke="#fff" stroke-width="1.2"/><path d="M5.8 8l1.5 1.5L10.3 6.5" stroke="#fff" stroke-width="1.1" fill="none"/></svg></span>

  <svg style="left:120px;top:141px" width="10" height="8" viewBox="0 0 10 8"><path d="M5 0l4 8-4-2.5L1 8z" fill="#F0AC33"/></svg>
  <svg style="left:246px;top:141px" width="10" height="8" viewBox="0 0 10 8"><path d="M5 0l4 8-4-2.5L1 8z" fill="#F0AC33"/></svg>
  <svg style="left:373px;top:141px" width="10" height="8" viewBox="0 0 10 8"><path d="M5 0l4 8-4-2.5L1 8z" fill="#2B2E31"/></svg>
  <p class="tl-label" style="left:125px;top:152px">100% exclusive<br>candidates</p>
  <p class="tl-label" style="left:251px;top:152px">Refundable<br>engagement fee</p>
  <p class="tl-label" style="left:378px;top:152px">Extended protection<br>&amp; post-placement<br>support</p>
</section>

<section class="slide col-l row-4">
  <div class="pattern-band"></div>
  <span class="bars"></span>
  <h2 class="title">How Our Partnership Works</h2>
  <p class="subtitle" style="top:36px">Who we help &amp; what success looks like</p>
  <div class="brand"><span class="mark"></span><span class="name">vemra</span></div>

  <span class="icon amber" style="left:22px;top:61px;width:31px;height:31px"><svg width="16" height="16" viewBox="0 0 16 16"><rect x="3" y="5" width="10" height="8" fill="none" stroke="#fff" stroke-width="1.2"/><path d="M3 5l5-3 5 3M6 8h1M9 8h1M6 10.5h1M9 10.5h1" stroke="#fff" stroke-width="1.1" fill="none"/></svg></span>
  <p class="group-head" style="left:64px;top:58px">Typical Clients:</p>
  <p class="group-list" style="left:64px;top:70px">• Hardware start-ups &amp; scale-ups<br>• Design consultancies<br>• Medtech &amp; consumer health brands</p>
  <div class="divider" style="left:22px;top:124px;width:184px;background:#eee"></div>
  <span class="icon dark" style="left:22px;top:145px;width:31px;height:31px"><svg width="16" height="16" viewBox="0 0 16 16"><path d="M4 13V9M7 13V7M10 13V10M13 13V5" stroke="#fff" stroke-width="1.6"/></svg></span>
  <p class="group-head" style="left:64px;top:142px">Challenges:</p>
  <p class="group-list" style="left:64px;top:154px">• Long hiring cycles<br>• Low candidate engagement<br>• Difficulty finding niche talent</p>

  <span class="icon orange" style="left:231px;top:61px;width:31px;height:31px"><svg width="16" height="16" viewBox="0 0 16 16"><circle cx="8" cy="5" r="2" fill="#fff"/><path d="M4 7l4 2 4-2-2 7H6z" fill="#fff"/></svg></span>
  <p class="group-head" style="left:273px;top:58px">What success looks like:</p>
  <p class="group-list" style="left:273px;top:70px">• Hiring within 3–6 weeks<br>• Candidates aligned &amp; excited<br>• Predictable process &amp; higher retention</p>
  <div class="photo-area" role="img" aria-label="Black and white photographs of product designers sketching and reviewing prototypes"></div>
</section>

<section class="slide col-r row-4">
  <div class="pattern-band"></div>
  <span class="bars"></span>
  <h2 class="title" style="left:21px">Call to Action</h2>
  <div class="brand"><span class="mark"></span><span class="name">vemra</span></div>
  <p class="cta-head">Ready to hire?</p>
  <p class="cta-sub">Let’s build your next great team together.</p>
  <p class="qmark" style="left:22px;top:68px">”</p>
  <p class="cta-quote">“Professional, personal, and focused—Vemra delivered exactly what we needed, and the hire exceeded expectations.”</p>
  <p class="cta-cite">— Aron Velkov, Founder, Plainform Studio</p>
  <a class="cta-btn">Book a Call</a>
  <div class="cta-visual" role="img" aria-label="Large amber and orange geometric brand graphic"></div>
</section>

</body>
</html>
```